New Business Cards For Urban Grow Store
Attention Grabber New High End Grow Store
New Business Cards For Urban Grow Store - Agriculture
Creative Brief
Bright & Fun-filled
The Hearthside Planter
Organic Specialist
4870 Pine Ridge Rd Columbia,Missouri 65203
1.877.Fe.Sprig
Bloom@TheHearthsidePlanter.example
TheHearthsidePlanter.example
Please place this on the front along the bottom please.."Custom Delveries Available "
www.TheHearthsidePlanter.example Bloom@TheHearthsidePlanter.example, 1.877.Fe.Sprig Besides the website email and phone number,Blank on back with lines to write notes.

```html
<!DOCTYPE html>
<html lang="en">
<head>
<meta charset="utf-8">
<title>The Hearthside Planter – Business Cards</title>
<link href="https://fonts.googleapis.com/css2?family=Open+Sans:wght@400;600;700;800&display=swap" rel="stylesheet">
<style>
  :root {
    --backdrop: #3b3b3d;
    --card-white: #ffffff;
    --leaf-green: #2f7a1f;
    --band-green: #3f8f22;
    --deep-green: #1f5a14;
    --orange: #e8711c;
    --orange-dark: #c85a10;
    --ink: #4a4a4a;
    --rule: #cfcfcf;
    --note-line: rgba(255,255,255,.55);
  }
  * { box-sizing: border-box; margin: 0; padding: 0; }
  html, body { width: 1200px; height: 871px; overflow: hidden; }
  body {
    background: var(--backdrop);
    font-family: "Open Sans", Arial, sans-serif;
    position: relative;
  }
  .card {
    position: absolute;
    width: 540px;
    height: 309px;
    border-radius: 14px;
    overflow: hidden;
    box-shadow: 0 10px 30px rgba(0,0,0,.45);
  }

  /* Back */
  .card-back {
    left: 330px; top: 110px;
    background: linear-gradient(160deg, var(--orange) 0%, var(--orange-dark) 100%);
  }
  .card-back .web {
    position: absolute; left: 34px; top: 40px;
    color: #fff; font-size: 15px; font-weight: 600; letter-spacing: .5px;
  }
  .notes {
    position: absolute; left: 34px; right: 34px; top: 100px;
    list-style: none;
  }
  .notes li {
    height: 36px;
    border-bottom: 1.5px solid var(--note-line);
  }

  /* Front */
  .card-front {
    left: 330px; top: 452px;
    background: var(--card-white);
  }
  .brand {
    position: absolute; left: 22px; top: 70px; width: 200px;
    display: flex; flex-direction: column; align-items: center; gap: 10px;
    text-align: center;
  }
  .brand-dot { width: 26px; height: 26px; border-radius: 50%; background: var(--orange); }
  .brand-name {
    color: var(--leaf-green); font-weight: 800; font-size: 24px; line-height: 1.1;
  }
  .brand-tagline {
    color: var(--orange); font-weight: 700; font-size: 12px; letter-spacing: 1px; text-transform: uppercase;
  }
  .divider {
    position: absolute; left: 240px; top: 38px; width: 1px; height: 200px; background: var(--rule);
  }
  .contact { position: absolute; left: 262px; top: 42px; color: var(--ink); }
  .contact .name { color: var(--deep-green); font-weight: 700; font-size: 19px; line-height: 1.1; }
  .contact .title { color: var(--orange); font-weight: 600; font-size: 11px; margin-top: 2px; }
  .contact .address { font-size: 11.5px; line-height: 1.45; margin-top: 22px; }
  .contact .lines { margin-top: 14px; list-style: none; font-size: 11.5px; line-height: 1.55; }
  .contact .lines li { display: flex; align-items: center; gap: 7px; }
  .contact .lines svg { width: 11px; height: 11px; fill: var(--deep-green); flex: none; }

  .band-accent {
    position: absolute; left: 0; right: 0; bottom: 34px; height: 4px; background: var(--orange);
  }
  .band {
    position: absolute; left: 0; right: 0; bottom: 0; height: 34px;
    background: var(--band-green);
    display: flex; align-items: center; justify-content: space-between;
    padding: 0 24px 0 60px;
  }
  .band .web { color: #fff; font-size: 12.5px; font-weight: 600; letter-spacing: 1.5px; }
  .band .delivery { color: #fff; font-size: 11.5px; font-weight: 700; letter-spacing: .5px; }
</style>
</head>
<body>

  <section class="card card-back">
    <p class="web">www.TheHearthsidePlanter.example</p>
    <ul class="notes" aria-label="Lines for notes">
      <li></li><li></li><li></li><li></li><li></li>
    </ul>
  </section>

  <section class="card card-front">
    <div class="brand">
      <span class="brand-dot"></span>
      <p class="brand-name">The Hearthside Planter</p>
      <p class="brand-tagline">Organic Specialist</p>
    </div>

    <div class="divider"></div>

    <div class="contact">
      <p class="name">Your name</p>
      <p class="title">Your Title</p>
      <p class="address">4870 Pine Ridge Rd<br>Columbia, Missouri 65203</p>
      <ul class="lines">
        <li>
          <svg viewBox="0 0 24 24" aria-hidden="true"><path d="M6.6 10.8a15.1 15.1 0 0 0 6.6 6.6l2.2-2.2a1 1 0 0 1 1-.25 11.4 11.4 0 0 0 3.6.57 1 1 0 0 1 1 1V20a1 1 0 0 1-1 1A17 17 0 0 1 3 4a1 1 0 0 1 1-1h3.5a1 1 0 0 1 1 1c0 1.25.2 2.45.57 3.57a1 1 0 0 1-.25 1z"/></svg>
          1.877.Fe.Sprig
        </li>
        <li>
          <svg viewBox="0 0 24 24" aria-hidden="true"><path d="M7 1h10a2 2 0 0 1 2 2v18a2 2 0 0 1-2 2H7a2 2 0 0 1-2-2V3a2 2 0 0 1 2-2zm0 3v14h10V4zm5 15.5a1 1 0 1 0 0 2 1 1 0 0 0 0-2z"/></svg>
          1.877.555.0142
        </li>
        <li>
          <svg viewBox="0 0 24 24" aria-hidden="true"><path d="M2 5h20v14H2zm2 2v.5l8 5 8-5V7zm0 2.9V17h16V9.9l-8 5z"/></svg>
          Bloom@TheHearthsidePlanter.example
        </li>
      </ul>
    </div>

    <div class="band-accent"></div>
    <div class="band">
      <p class="web">TheHearthsidePlanter.example</p>
      <p class="delivery">Custom Deliveries Available</p>
    </div>
  </section>

</body>
</html>
```